Need a business card for our overland brand!

We had the logo made and we need a great design for our business card. Use the logo provide or tweak it however you see fit.

Contact Information for Business Card

Name, Title, Telephone, email, website

```html
<!DOCTYPE html>
<html lang="en">
<head>
<meta charset="utf-8">
<title>Summit Trail — Business Card</title>
<link rel="stylesheet" href="https://fonts.googleapis.com/css2?family=Barlow+Condensed:wght@400;500;600;800&display=swap">
<style>
  :root {
    --backdrop: #c7cbce;
    --navy: #243750;
    --accent-blue: #1f93b8;
    --paper: #f6f6f4;
    --ink: #2a2f36;
    --shadow: rgba(20, 30, 40, 0.22);
  }
  * { margin: 0; padding: 0; box-sizing: border-box; }
  html, body {
    width: 1200px;
    height: 1038px;
    overflow: hidden;
    background: var(--backdrop);
    font-family: "Barlow Condensed", "Arial Narrow", sans-serif;
  }
  .canvas {
    position: relative;
    width: 1200px;
    height: 1038px;
  }
  .card {
    position: absolute;
    left: 250px;
    width: 700px;
    height: 400px;
    overflow: hidden;
    box-shadow: 0 10px 28px var(--shadow);
  }
  .card--front {
    top: 79px;
    background: var(--navy);
    display: flex;
    align-items: center;
    justify-content: center;
  }
  .card--back {
    top: 559px;
    background: var(--paper);
  }
  .brand-name {
    font-weight: 800;
    text-transform: uppercase;
    line-height: 0.88;
    letter-spacing: 1px;
  }
  .card--front .brand-name {
    color: var(--paper);
    font-size: 108px;
    text-align: center;
  }
  .card--back .brand-name {
    position: absolute;
    left: 62px;
    bottom: 54px;
    color: var(--navy);
    font-size: 58px;
  }
  .holder {
    position: absolute;
    left: 340px;
    top: 62px;
    color: var(--accent-blue);
    text-transform: uppercase;
  }
  .holder-name {
    font-weight: 600;
    font-size: 40px;
    letter-spacing: 1px;
    line-height: 1;
  }
  .holder-title {
    font-weight: 400;
    font-size: 22px;
    margin-top: 10px;
    letter-spacing: 1px;
  }
  .contact-list {
    position: absolute;
    left: 340px;
    top: 170px;
    list-style: none;
  }
  .contact-rail {
    position: absolute;
    left: 13px;
    top: -14px;
    width: 3px;
    height: 160px;
    background: var(--navy);
  }
  .contact-item {
    position: relative;
    display: flex;
    align-items: center;
    gap: 14px;
    height: 44px;
    color: var(--ink);
    font-size: 24px;
    font-weight: 400;
  }
  .contact-icon {
    width: 29px;
    height: 29px;
    border-radius: 50%;
    background: var(--paper);
    border: 2px solid var(--navy);
    display: flex;
    align-items: center;
    justify-content: center;
    flex: none;
  }
  .accent-band {
    position: absolute;
    right: 0;
    top: 40px;
    width: 24px;
    height: 270px;
    background: var(--accent-blue);
  }
  .accent-foot {
    position: absolute;
    right: 0;
    bottom: 0;
    width: 24px;
    height: 90px;
    background: var(--navy);
  }
</style>
</head>
<body>
<main class="canvas">

  <section class="card card--front" aria-label="Business card front">
    <h1 class="brand-name">Summit<br>Trail</h1>
  </section>

  <section class="card card--back" aria-label="Business card back">
    <div class="holder">
      <p class="holder-name">Dana Reyes</p>
      <p class="holder-title">CEO</p>
    </div>

    <ul class="contact-list">
      <li class="contact-rail" aria-hidden="true"></li>
      <li class="contact-item">
        <span class="contact-icon">
          <svg width="13" height="16" viewBox="0 0 13 16" aria-hidden="true">
            <rect x="1.5" y="1" width="10" height="14" rx="1.5" fill="none" stroke="#243750" stroke-width="1.6"/>
            <line x1="5" y1="12.2" x2="8" y2="12.2" stroke="#243750" stroke-width="1.4"/>
          </svg>
        </span>
        <span>555-014-2290</span>
      </li>
      <li class="contact-item">
        <span class="contact-icon">
          <svg width="16" height="12" viewBox="0 0 16 12" aria-hidden="true">
            <rect x="1" y="1" width="14" height="10" fill="none" stroke="#243750" stroke-width="1.6"/>
            <polyline points="1,1 8,7 15,1" fill="none" stroke="#243750" stroke-width="1.6"/>
          </svg>
        </span>
        <span>dana@summittrail.com</span>
      </li>
      <li class="contact-item">
        <span class="contact-icon">
          <svg width="16" height="16" viewBox="0 0 16 16" aria-hidden="true">
            <circle cx="8" cy="8" r="6.5" fill="none" stroke="#243750" stroke-width="1.5"/>
            <ellipse cx="8" cy="8" rx="3" ry="6.5" fill="none" stroke="#243750" stroke-width="1.3"/>
            <line x1="1.5" y1="8" x2="14.5" y2="8" stroke="#243750" stroke-width="1.3"/>
          </svg>
        </span>
        <span>summittrail.com</span>
      </li>
    </ul>

    <p class="brand-name">Summit<br>Trail</p>

    <div class="accent-band" aria-hidden="true"></div>
    <div class="accent-foot" aria-hidden="true"></div>
  </section>

</main>
</body>
</html>
```